Website Design for BRAVO FREIGHTWAY

Hello. We are a Freight Brokage business in the transportation and logistics industry in the USA. Company name is BRAVO FREIGHTWAY. I'm looking to have a 5 page or less website built. Must have HOME, SHIPPERS, CARRIERS, ABOUT and CONTACT US.. I have additional information that needs to be placed in the footer of the website. Company address, contact info privacy and terms and conditions Need nice, vibrant looking site. The website needs to be a fully functionable site that is built and coded for wordpress and ready for hosting. Please visit these link for you to have an idea of the look and feel I want. www.tolvanhaulage.example www.corvel-transit.example. Will have logo concept in 2 days for upload. As time goes by I will supply more content and the layout of the respective pages.

```html
<!DOCTYPE html>
<html lang="en">
<head>
<meta charset="utf-8">
<title>Bravo Freightway</title>
<link href="https://fonts.googleapis.com/css2?family=Poppins:wght@400;500;600;700&family=Lato:wght@400;700&display=swap" rel="stylesheet">
<style>
:root{
  --red:#f0402f;
  --red-dark:#d9331f;
  --ink:#151515;
  --body:#333;
  --light:#f3f3f3;
  --white:#fff;
  --footer:#1c1c1c;
}
*{box-sizing:border-box;margin:0;padding:0}
html,body{width:1200px;height:3283px;overflow:hidden}
body{font-family:'Lato',sans-serif;color:var(--body);background:var(--white);position:relative}
section,footer,header{position:absolute;left:0;width:1200px}
.abs{position:absolute}
h2.section-title{position:absolute;left:0;width:1200px;text-align:center;font-family:'Poppins',sans-serif;font-weight:600;font-size:36px;line-height:51px;color:var(--ink)}
h2.section-title em{font-style:normal;color:var(--red)}
.title-rule{position:absolute;left:515px;width:170px;height:2px;background:#e2e2e2}
.title-rule::after{content:"";position:absolute;left:55px;top:-2px;width:60px;height:6px;background:var(--red)}
.brand{font-family:'Poppins',sans-serif;font-weight:700;font-size:20px;color:var(--white);display:flex;align-items:center;gap:8px}
.brand-mark{width:14px;height:14px;background:var(--red)}

/* Hero */
.hero{top:0;height:615px;background:linear-gradient(90deg,#1d1b19 0%,#2a2520 40%,#3b2a1c 62%,#7a4a1c 100%);overflow:hidden}
.hero-photo{position:absolute;left:420px;top:0;width:780px;height:615px;background:linear-gradient(160deg,#b5661d 0%,#5c3a20 35%,#1f232b 65%,#2b2b2e 100%)}
.hero-shade{position:absolute;left:0;top:0;width:700px;height:615px;background:linear-gradient(90deg,rgba(20,19,18,.95) 55%,rgba(20,19,18,0))}
.nav{position:absolute;left:458px;top:31px;display:flex;gap:34px;font-size:15px;color:var(--white)}
.nav a{color:var(--white);text-decoration:none}
.nav a.active{font-weight:700;text-decoration:underline}
.phone-btn{position:absolute;left:918px;top:22px;width:170px;height:40px;background:var(--red);color:var(--white);font-weight:700;font-size:16px;display:flex;align-items:center;justify-content:center;gap:10px;transform:skewX(-8deg)}
.phone-btn span,.phone-btn svg{transform:skewX(8deg)}
.hero-kicker{left:112px;top:166px;font-family:'Poppins',sans-serif;font-weight:600;font-size:21px;letter-spacing:2px;color:var(--white)}
.hero-title{left:110px;top:194px;font-family:'Poppins',sans-serif;font-weight:600;font-size:56px;color:var(--white);line-height:70px}
.hero-text{left:112px;top:272px;width:410px;font-size:15px;line-height:26px;color:#eee}
.btn{position:absolute;height:44px;display:flex;align-items:center;justify-content:center;font-weight:700;font-size:15px;transform:skewX(-8deg);box-shadow:4px 4px 0 rgba(255,255,255,.9)}
.btn span{transform:skewX(8deg)}
.btn-red{background:var(--red);color:var(--white)}
.btn-white{background:var(--white);color:var(--red);box-shadow:4px 4px 0 var(--red)}
.dots{left:114px;top:442px;display:flex;gap:10px}
.dots i{width:9px;height:9px;border-radius:50%;background:#888;display:block}
.dots i.on{background:var(--white)}
.partners{left:112px;top:528px;width:976px;display:flex;justify-content:space-between;align-items:center}
.partner{width:112px;height:44px;border:2px solid rgba(255,255,255,.55);border-radius:6px}

/* Services */
.services{top:615px;height:676px}
.services .lead{position:absolute;top:188px;width:1200px;text-align:center;font-size:15px}
.card{position:absolute;top:259px;width:222px;height:316px;background:var(--ink);color:var(--white);text-align:center;padding:30px 16px 0}
.card h3{font-family:'Poppins',sans-serif;font-weight:500;font-size:18px;line-height:27px;margin:14px 0 10px}
.card p{font-size:15px;line-height:29px}
.card .go{position:absolute;left:50%;bottom:16px;transform:translateX(-50%)}
.card.featured{top:233px;left:600px;width:248px;height:368px;background:linear-gradient(180deg,#f0402f,#e2402f);box-shadow:0 8px 20px rgba(0,0,0,.2)}
.slider-arrow{position:absolute;top:401px;width:34px;height:34px;border-radius:50%;background:#666;display:flex;align-items:center;justify-content:center}

/* About */
.about{top:1291px;height:652px;background:linear-gradient(135deg,#f14a35,#ee3f2b 60%,#e8422f)}
.about-band{position:absolute;left:0;top:219px;width:411px;height:433px;background:#f2a9a0}
.about .section-title{color:var(--white);top:40px}
.about .title-rule{background:rgba(255,255,255,.35)}
.about .title-rule::after{background:var(--white)}
.about-photo{position:absolute;left:112px;top:150px;width:418px;height:427px;border:4px solid var(--white);background:linear-gradient(135deg,#7f2a24,#b8432f 40%,#5a4a3c 70%,#2f3a4f)}
.about-text{position:absolute;left:599px;top:143px;width:490px;color:var(--white);font-size:15px;line-height:29.2px;text-align:justify}
.about-text p+p{margin-top:29px}
.read-more{left:600px;top:531px;width:146px;height:42px;background:var(--white);color:var(--red);box-shadow:4px 4px 0 rgba(0,0,0,.15)}

/* Stats */
.stats{top:1943px;height:376px}
.stat{position:absolute;top:160px;width:240px;text-align:center}
.stat b{display:block;font-family:'Poppins',sans-serif;font-weight:700;font-size:52px;line-height:58px;color:var(--red)}
.stat span{display:block;font-size:16px;line-height:26px;color:var(--ink);margin-top:4px}
.divider{position:absolute;top:143px;width:2px;height:172px;background:#ddd}
.divider::after{content:"";position:absolute;left:-5px;top:81px;width:12px;height:12px;border-radius:50%;background:var(--red)}

/* Testimonials */
.reviews{top:2319px;height:535px;background:var(--light)}
.person{position:absolute;left:112px;width:339px;height:100px;display:flex;align-items:center;padding-left:22px;gap:22px}
.person.active{background:var(--white);border:2px solid var(--red);box-shadow:0 6px 16px rgba(0,0,0,.08)}
.avatar{width:66px;height:66px;border-radius:50%;background:linear-gradient(135deg,#c9b3a0,#6b5446)}
.person h4{font-family:'Poppins',sans-serif;font-weight:500;font-size:21px;color:var(--ink)}
.person.active h4{color:var(--red);text-transform:uppercase}
.person small{font-family:'Poppins',sans-serif;font-weight:500;font-size:11px;color:#444}
.quote{position:absolute;left:560px;top:140px;width:530px}
.quote h4{font-family:'Poppins',sans-serif;font-weight:600;font-size:24px;color:var(--ink)}
.quote h4 small{font-size:12px;font-weight:500;color:#555;margin-left:8px}
.stars{color:#f5b72e;font-size:20px;letter-spacing:1px;margin:8px 0 6px}
.quote p{font-size:15px;line-height:31px;color:#333}
.quote p+p{margin-top:31px}
.quote .thanks{color:var(--red);font-weight:700;font-size:17px;margin-top:12px}

/* Footer */
.site-footer{top:2854px;height:429px;background:var(--footer);color:var(--white)}
.site-footer h5{font-family:'Poppins',sans-serif;font-weight:600;font-size:21px;margin-bottom:18px}
.socials{left:112px;top:144px;display:flex;gap:13px}
.socials i{width:30px;height:30px;background:var(--red);display:block}
.subscribe{left:347px;top:60px;width:240px}
.subscribe p{font-size:13px;line-height:25px;padding-left:7px;margin-top:-4px}
.subscribe .field{margin:14px 0 0 7px;width:229px;height:46px;background:var(--white);color:#888;font-size:13px;padding:15px 18px}
.subscribe .submit{margin:22px 0 0 7px;width:186px;height:55px;background:var(--red);font-size:17px;font-weight:700;padding:17px 18px}
.contact{left:614px;top:60px;width:330px}
.contact li{list-style:none;display:flex;gap:14px;font-size:15px;line-height:27px;margin-bottom:10px}
.contact li i{flex:none;width:30px;height:30px;background:var(--red);display:flex;align-items:center;justify-content:center;margin-top:4px}
.quick{left:971px;top:60px}
.quick li{list-style:none;font-size:15px;line-height:34px;display:flex;align-items:center;gap:10px}
.footer-rule{left:112px;top:346px;width:976px;height:1px;background:#555}
.legal{left:112px;top:382px;width:976px;display:flex;justify-content:space-between;font-size:14px}
.legal nav{display:flex;gap:28px}
.legal nav span.sep{color:#666}
</style>
</head>
<body>

<header class="hero">
  <div class="hero-photo" role="img" aria-label="Photo of a dark semi truck with a white trailer on a desert highway at sunset"></div>
  <div class="hero-shade"></div>
  <div class="brand abs" style="left:112px;top:34px"><i class="brand-mark"></i>Bravo Freightway</div>
  <nav class="nav">
    <a class="active">Home</a><a>Shippers</a><a>Carriers</a><a>About</a><a>Contact Us</a>
  </nav>
  <div class="phone-btn"><svg width="18" height="18" viewBox="0 0 24 24"><rect width="24" height="24" rx="4" fill="#fff"/><path d="M8 5l3 3-2 2c1 2 3 4 5 5l2-2 3 3-2 3C10 19 5 14 5 7z" fill="#f0402f"/></svg><span>555-014-2290</span></div>
  <div class="hero-kicker abs">Welcome to</div>
  <h1 class="hero-title abs">Bravo Freightway</h1>
  <p class="hero-text abs">Itaque earum rerum hic tenetur a sapiente delectus, ut aut reiciendis voluptatibus maiores alias consequatur aut perferendis doloribus asperiores repellat.</p>
  <div class="btn btn-red" style="left:116px;top:366px;width:106px"><span>Carriers</span></div>
  <div class="btn btn-white" style="left:244px;top:366px;width:114px"><span>Customers</span></div>
  <div class="dots abs"><i></i><i></i><i class="on"></i><i></i></div>
  <div class="partners abs" aria-label="Partner badges">
    <div class="partner" style="width:76px;border-radius:50%"></div><div class="partner"></div><div class="partner" style="width:90px"></div><div class="partner" style="width:106px"></div><div class="partner" style="width:132px"></div><div class="partner" style="width:116px"></div>
  </div>
</header>

<section class="services">
  <h2 class="section-title" style="top:43px">Full truckload solutions that <em>help you</em><br><em>deliver</em> on your <em>promises</em></h2>
  <div class="title-rule" style="top:158px"></div>
  <p class="lead">Our extensive network of capacity stands ready to deliver your cargo on time every time!</p>

  <div class="slider-arrow" style="left:39px"><svg width="12" height="14" viewBox="0 0 12 14"><path d="M9 1L3 7l6 6" stroke="#fff" stroke-width="2.5" fill="none"/></svg></div>
  <div class="slider-arrow" style="left:1124px"><svg width="12" height="14" viewBox="0 0 12 14"><path d="M3 1l6 6-6 6" stroke="#fff" stroke-width="2.5" fill="none"/></svg></div>

  <article class="card" style="left:111px">
    <svg width="64" height="78" viewBox="0 0 64 78" fill="none" stroke="#fff" stroke-width="2.5"><circle cx="32" cy="46" r="28"/><ellipse cx="32" cy="46" rx="12" ry="28"/><path d="M4 46h56M8 32h48M8 60h48"/><circle cx="32" cy="16" r="12" fill="#151515" stroke="#f0402f"/></svg>
    <h3>National &amp; Regional Capacity</h3>
    <p>Direct access to over 100 national, regional &amp; local LTL carriers</p>
    <svg class="go" width="22" height="22" viewBox="0 0 22 22"><circle cx="11" cy="11" r="11" fill="#f0402f"/><path d="M6 11h9M11 7l4 4-4 4" stroke="#fff" stroke-width="2.2" fill="none"/></svg>
  </article>
  <article class="card" style="left:357px">
    <svg width="80" height="76" viewBox="0 0 80 76" fill="none" stroke="#fff" stroke-width="2.5"><circle cx="30" cy="12" r="9" stroke="#f0402f"/><circle cx="54" cy="12" r="9" stroke="#f0402f"/><circle cx="14" cy="40" r="9"/><circle cx="42" cy="40" r="9"/><path d="M8 74V54h12v20M36 74V54h12v20M56 74V30h10v44M64 74V24M2 74h76"/></svg>
    <h3>Competitive Prices</h3>
    <p>We leverage our purchasing volume to drive down costs</p>
    <svg class="go" width="22" height="22" viewBox="0 0 22 22"><circle cx="11" cy="11" r="11" fill="#f0402f"/><path d="M6 11h9M11 7l4 4-4 4" stroke="#fff" stroke-width="2.2" fill="none"/></svg>
  </article>
  <article class="card featured">
    <svg width="80" height="76" viewBox="0 0 80 76" fill="none" stroke="#fff" stroke-width="2.5"><circle cx="30" cy="18" r="13"/><path d="M6 72V54c0-8 8-14 16-14h14"/><circle cx="54" cy="52" r="20"/><path d="M54 40v12l8 6"/></svg>
    <h3 style="font-weight:600;font-size:19px">Dedicated Representatives</h3>
    <p>A Dedicated representative that knows your business &amp; can easily troubleshoot shipment issues without your involvement.</p>
    <svg class="go" width="22" height="22" viewBox="0 0 22 22"><circle cx="11" cy="11" r="11" fill="#fff"/><path d="M6 11h9M11 7l4 4-4 4" stroke="#f0402f" stroke-width="2.2" fill="none"/></svg>
  </article>
  <article class="card" style="left:865px">
    <svg width="80" height="76" viewBox="0 0 80 76" fill="none" stroke="#fff" stroke-width="2.5"><path d="M14 40V32a26 26 0 0152 0v8"/><rect x="6" y="38" width="12" height="22" rx="4"/><rect x="62" y="38" width="12" height="22" rx="4"/><path d="M68 60c0 8-10 12-20 12"/><circle cx="40" cy="36" r="9" stroke="#f0402f"/><path d="M36 46h8M37 51h6" stroke="#f0402f"/></svg>
    <h3>Proactive communication</h3>
    <p>Proactive communication with LTL carriers, problem resolutions, &amp;</p>
    <svg class="go" width="22" height="22" viewBox="0 0 22 22"><circle cx="11" cy="11" r="11" fill="#f0402f"/><path d="M6 11h9M11 7l4 4-4 4" stroke="#fff" stroke-width="2.2" fill="none"/></svg>
  </article>
</section>

<section class="about">
  <div class="about-band"></div>
  <h2 class="section-title">About Bravo Freightway</h2>
  <div class="title-rule" style="top:106px"></div>
  <div class="about-photo" role="img" aria-label="Photo of two smiling truck drivers in caps standing in front of red trucks"></div>
  <div class="about-text">
    <p>At vero eos et accusamus et iusto odio dignissimos ducimus qui blanditiis praesentium voluptatum deleniti atque corrupti quos dolores et quas molestias excepturi sint occaecati cupiditate non provident, similique sunt in culpa qui officia deserunt mollitia animi, id est laborum et dolorum fuga. Et harum quidem rerum facilis est et expedita distinctio.</p>
    <p>Nam libero tempore, cum soluta nobis est eligendi optio cumque nihil impedit quo minus id quod maxime placeat facere possimus, omnis voluptas assumenda est, omnis dolor repellendus. Temporibus autem quibusdam et aut officiis debitis aut rerum necessitatibus saepe eveniet ut et voluptates repudiandae sint et molestiae non recusandae. Itaque earum rerum hic tenetur a sapiente delectus, ut aut reiciendis voluptatibus maior doloribus asperiores repellat.</p>
  </div>
  <div class="btn read-more"><span>Read More</span></div>
</section>

<section class="stats">
  <h2 class="section-title" style="top:44px">Trusted by <em>750+ happy clients</em></h2>
  <div class="title-rule" style="top:109px"></div>
  <div class="stat" style="left:60px"><b>15+</b><span>Over a Decade of<br>Experience</span></div>
  <div class="divider" style="left:308px"></div>
  <div class="stat" style="left:331px"><b>98%</b><span>Hundreds of Happy Clients<br>with 98% Success Rate</span></div>
  <div class="divider" style="left:600px"></div>
  <div class="stat" style="left:614px"><b>75 Yr</b><span>Built on 75 Years of<br>Research</span></div>
  <div class="divider" style="left:857px"></div>
  <div class="stat" style="left:869px"><b>30+</b><span>Certified in Awards<br>Rewards</span></div>
</section>

<section class="reviews">
  <h2 class="section-title" style="top:35px">What <em>Customer Says</em></h2>
  <div class="title-rule" style="top:101px"></div>
  <div class="person" style="top:134px"><div class="avatar" role="img" aria-label="Portrait photo of a client"></div><div><h4>Dana Morrow</h4><small>Senior Manager, United States</small></div></div>
  <div class="person active" style="top:266px"><div class="avatar" role="img" aria-label="Portrait photo of a client"></div><div><h4>Omar Vance</h4><small>Assistant Manager, United States</small></div></div>
  <div class="person" style="top:384px"><div class="avatar" role="img" aria-label="Portrait photo of a client"></div><div><h4>Dana Morrow</h4><small>Senior Manager, United States</small></div></div>
  <div class="quote">
    <h4>Omar Vance<small>(Assistant Manager, United States)</small></h4>
    <div class="stars">★★★★★</div>
    <p>Temporibus autem quibusdam et aut officiis debitis aut rerum necessitatibus saepe eveniet ut et voluptates repudiandae sint et molestiae non recusandae.</p>
    <p>Itaque earum rerum hic tenetur a sapiente delectus, ut aut reiciendis voluptatibus maiut officiis debitis aut rerum necessitatibus saepe eveniet ut a sapiente delectus, ut aut reiciendis voluptatibusores alias consequatur aut perferendis doloribus asperiores repellat.</p>
    <p class="thanks" style="margin-top:12px">Thanks, Bravo Freightway</p>
  </div>
</section>

<footer class="site-footer">
  <div class="brand abs" style="left:112px;top:90px"><i class="brand-mark"></i>Bravo Freightway</div>
  <div class="socials abs" aria-label="Social links"><i></i><i></i><i></i><i></i></div>
  <div class="subscribe abs">
    <h5>Subscribe Us</h5>
    <p>Itaque earum rerum hic tenetur a voluptatibus maiores aliasr</p>
    <div class="field">Enter The Email</div>
    <div class="submit">Subscribe</div>
  </div>
  <div class="contact abs">
    <h5>Contact Us</h5>
    <ul>
      <li><i><svg width="12" height="16" viewBox="0 0 12 16"><path d="M6 0a6 6 0 016 6c0 4-6 10-6 10S0 10 0 6a6 6 0 016-6z" fill="#fff"/><circle cx="6" cy="6" r="2" fill="#f0402f"/></svg></i><span>Bravo Freightway, LLC 418 N Alder Ridge Ave Suite 3107 Marlow, WA 99210</span></li>
      <li><i><svg width="14" height="14" viewBox="0 0 24 24"><path d="M6 2l4 4-2 3c1 3 4 6 7 7l3-2 4 4-3 4C10 22 2 14 2 5z" fill="#fff"/></svg></i><span style="padding-top:4px">555-014-2290</span></li>
      <li><i><svg width="12" height="16" viewBox="0 0 12 16"><path d="M6 0a6 6 0 016 6c0 4-6 10-6 10S0 10 0 6a6 6 0 016-6z" fill="#fff"/><circle cx="6" cy="6" r="2" fill="#f0402f"/></svg></i><span>7410 Cedar Point Rd NE Suite 902<br>Halvern, WA 98140</span></li>
      <li><i><svg width="14" height="11" viewBox="0 0 14 11"><rect width="14" height="11" fill="#fff"/><path d="M0 0l7 6 7-6" stroke="#f0402f" fill="none"/></svg></i><span style="padding-top:4px">support@bravofreightway.example</span></li>
    </ul>
  </div>
  <div class="quick abs">
    <h5>Quick Links</h5>
    <ul>
      <li><svg width="13" height="12" viewBox="0 0 13 12"><path d="M0 6h10M6 1l5 5-5 5" stroke="#fff" stroke-width="2.4" fill="none"/></svg>Home</li>
      <li><svg width="13" height="12" viewBox="0 0 13 12"><path d="M0 6h10M6 1l5 5-5 5" stroke="#fff" stroke-width="2.4" fill="none"/></svg>Shippers</li>
      <li><svg width="13" height="12" viewBox="0 0 13 12"><path d="M0 6h10M6 1l5 5-5 5" stroke="#fff" stroke-width="2.4" fill="none"/></svg>Carriers</li>
      <li><svg width="13" height="12" viewBox="0 0 13 12"><path d="M0 6h10M6 1l5 5-5 5" stroke="#fff" stroke-width="2.4" fill="none"/></svg>About Us</li>
      <li><svg width="13" height="12" viewBox="0 0 13 12"><path d="M0 6h10M6 1l5 5-5 5" stroke="#fff" stroke-width="2.4" fill="none"/></svg>Contact Us</li>
    </ul>
  </div>
  <div class="footer-rule abs"></div>
  <div class="legal abs">
    <span>Copyrights@2023.Bravo Freightway.All Rights Reserved</span>
    <nav><span>Privacy</span><span class="sep">|</span><span>Terms and Conditions</span></nav>
  </div>
</footer>

</body>
</html>
```